[Design ONLY] Design for our Ecommerce business website

We require a web design for our ecommerce business website. We sell textbooks, Computer & Accessories, Gifts and stationery and Laptop/IT support service etc
Requirement:
We Require 3 pages for each design: Homepage, Product page and Payment page
Design Approach:
Design UI to be have a modern and professional feel and user experience must be good.
Responsive web design approach.
1. Home page
- Logo/Heading
- Navigation links to other pages eg. About us
- Appropriate images/banners
- A special offer
- Recent News
Include an overview of the business:
- provide general information
- contact information
- links to social media
- Frequently Asked Questions (FAQ) page
Publish store policies and make sure they are not too difficult to find:
- shipping and return policies
- outline the return process and what products can be returned
- provide easy access to a privacy policy that covers shoppers’ personal and financial information (this is crucial)
2. Product
Product Pages should include:
- Pictures, descriptions, order and price information for your products and/or services.
- Navigation links to other pages, especially home, about us, order and other product pages.
- Links to a shopping cart
- Add to wishlist
- Related or recommend products
3. Payment
- Standard payment form with payment integration with Brenox and Lumbix.
- Shipping or Self Collection fee
User Experience Aspect:
Well-Defined Product Categories
a. The top level of navigation should show the set of categories that the site offers. Group products into categories and subcategories. Category labels work best as single words that describe the range of products, so shoppers can scan through them and instantly understand what they represent.
Product Search
a. Build a search function that helps them easily find what they are looking for.
Make search omnipresent: Put the search box on every page and in familiar locations. The box should be visible, quickly recognizable, and easy to use.
b. Allow sorting and filtering of results: Let shoppers sort search results based on various criteria (best sellers, highest or lowest price, product rating, newest item, etc.) as well as eliminate items that do not fit within a certain category.
Product Quick view
a. A “quick view” reduces the time it takes for shoppers to find the right product by eliminating unnecessary page loads. Also, be sure to include a prominently positioned “Add to Cart” button as well as a “Save to Wishlist” functionality.
b. Show Related and Recommended Products. This can be displayed on a product detail page.
Target Market(s)
university students
Number of Pages Required
3 page
Requirements
Must have
- Note * its a university store. not a normal ecommerce shop*
Do include design for the 3 pages specified. Homepage, product page and payment page.

```html
<!DOCTYPE html>
<html lang="en">
<head>
<meta charset="utf-8">
<title>ELM COOP – Payment</title>
<link href="https://fonts.googleapis.com/css2?family=Roboto:wght@400;500;700&display=swap" rel="stylesheet">
<style>
:root{
  --blue:#1565c0;
  --navy:#1d2656;
  --ink:#2b2f38;
  --muted:#9aa0ab;
  --line:#e8eaef;
  --page:#f5f6f9;
  --dark:#2d2f33;
  --foot:#3f4450;
  --peach:#fef6ee;
}
*{box-sizing:border-box;margin:0;padding:0}
html,body{width:1200px;height:1200px;overflow:hidden;background:#fff;font-family:'Roboto',sans-serif;color:var(--ink)}
.stage{position:absolute;left:0;top:0;width:1932px;height:1932px;transform:scale(.62112);transform-origin:0 0}
.abs{position:absolute}
.deco{position:absolute;left:0;top:0}

.brand{position:absolute;color:var(--navy);font-weight:500;line-height:.9;letter-spacing:-1px}
.brand-hero{left:175px;top:125px;font-size:72px}
.kicker{left:422px;top:124px;font-size:24px;font-weight:500;color:var(--blue)}
.title{left:420px;top:152px;font-size:62px;font-weight:700;color:var(--blue)}

.badge{position:absolute;width:96px;height:96px;border-radius:50%;background:var(--blue);color:#fff;font-size:40px;font-weight:500;display:flex;align-items:center;justify-content:center;box-shadow:0 0 0 8px #fff}

.panel{position:absolute;width:742px;background:var(--page);overflow:hidden;box-shadow:0 14px 40px rgba(40,70,140,.08)}
.panel > *{position:absolute}

/* header */
.topbar{left:0;top:0;width:100%;height:19px;background:var(--blue)}
.topbar span{position:absolute;top:5px;font-size:5px;color:#fff}
.masthead{left:0;top:19px;width:100%;height:58px;background:#fff}
.masthead .brand{left:144px;top:12px;font-size:17px;letter-spacing:0}
.acct{position:absolute;top:25px;font-size:5px;color:var(--ink);display:flex;align-items:center;gap:10px}
.acct i{width:9px;height:9px;border:1.2px solid var(--blue);border-radius:2px;display:block;position:relative}
.acct b{position:absolute;top:-5px;right:-5px;width:6px;height:6px;border-radius:50%;background:var(--blue)}
.navband{left:0;top:77px;width:100%;height:35px;background:var(--dark)}
.navbar{position:absolute;left:145px;top:9px;width:452px;height:18px;background:#fff;border-radius:1px;display:flex;align-items:center;font-size:5.2px;font-weight:500}
.navbar .menu{width:18px;height:18px;background:var(--blue);color:#fff;font-size:8px;display:flex;align-items:center;justify-content:center;margin-right:13px;letter-spacing:-.5px}
.navbar a{color:var(--ink);text-decoration:none;margin-right:12px}
.navbar a.on{color:var(--blue)}
.navbar .find{margin-left:auto;color:#c3c6cc;font-weight:400;margin-right:22px}
.navbar svg{position:absolute;right:6px;top:5px}
.crumb{left:0;top:112px;width:100%;height:58px;background:#fff;font-size:8.5px;text-align:center;line-height:58px;color:#555}

/* cards */
.card{background:#fff;width:584px;left:79px}
.step{position:absolute;top:24px;height:30px}
.step .dot{position:absolute;left:0;top:0;width:30px;height:30px;border-radius:50%;border:1px solid #eceef2;display:flex;align-items:center;justify-content:center}
.step .dot.on{background:var(--blue);border-color:var(--blue)}
.step small{position:absolute;left:47px;top:5px;font-size:4.5px;letter-spacing:.5px;color:#c0c4cb;white-space:nowrap;font-weight:500}
.step span{position:absolute;left:47px;top:15px;font-size:7px;color:var(--ink);white-space:nowrap}

.lbl{position:absolute;font-size:6px;color:#333}
.field{position:absolute;height:27px;border:1px solid var(--line);font-size:6px;color:#555;padding-left:10px;line-height:25px;background:#fff}
.field.sel::after{content:"";position:absolute;right:9px;top:10px;width:3px;height:3px;border-right:1px solid #999;border-bottom:1px solid #999;transform:rotate(45deg)}
.rule{height:1px;background:var(--line);left:0;width:100%}
.btn{position:absolute;height:26px;font-size:5.5px;font-weight:700;letter-spacing:.8px;display:flex;align-items:center;justify-content:center;gap:7px}
.btn.ghost{border:1px solid var(--line);color:#b4b8bf;background:#fff}
.btn.solid{background:var(--blue);color:#fff}

.pay{position:absolute;top:15px;width:25px;height:16px;border-radius:1px;color:#fff;font-size:4.5px;font-weight:700;display:flex;align-items:center;justify-content:center}

.sec{position:absolute;font-size:5.5px;font-weight:700;letter-spacing:1px;color:#a9aeb6}
.row{position:absolute;font-size:7px;color:var(--ink);white-space:nowrap}
.row.m{color:var(--muted)}
.row.r{text-align:right}
.cap{position:absolute;font-size:6px;color:#b2b6bd}

.opt{position:absolute;width:135px;height:47px;border:1px solid var(--line);background:#fff}
.opt.on{border-color:var(--blue)}
.opt em{position:absolute;left:15px;top:13px;font-style:normal;font-size:7px;color:#777}
.opt small{position:absolute;left:15px;top:26px;font-size:5px;color:#aaa}
.opt strong{position:absolute;right:15px;top:17px;font-size:10px;font-weight:400;color:#555}
.opt.on em,.opt.on strong,.opt.on small{color:var(--blue)}

.foot-col{position:absolute;top:20px;font-size:4px;line-height:10px;color:#c7cad2}
.foot-col b{display:block;font-size:5.5px;color:#fff;margin-bottom:2px}
</style>
</head>
<body>
<div class="stage">

  <svg class="deco" width="1932" height="1932" viewBox="0 0 1932 1932" aria-hidden="true">
    <path d="M840 190 C980 140 1500 120 1760 260 C1950 360 1960 700 1880 980 C1820 1200 1700 1500 1400 1700 C1200 1830 1000 1900 1100 1932 L300 1932 C380 1800 520 1500 700 1300 C860 1120 1000 900 920 760 C820 580 760 230 840 190 Z" fill="var(--peach)"/>
    <path d="M1760 900 C1830 940 1790 1150 1720 1300 L1690 1300 C1720 1150 1740 960 1760 900 Z" fill="#fdf1f2"/>
    <circle cx="406" cy="6" r="25" fill="var(--blue)"/>
    <circle cx="306" cy="14" r="3" fill="#d7f3ea"/>
    <circle cx="139" cy="969" r="7" fill="none" stroke="var(--blue)" stroke-width="1.5"/>
    <circle cx="107" cy="707" r="11" fill="none" stroke="#c9f2e1" stroke-width="3"/>
    <path d="M150 513 l8 8 M158 513 l-8 8" stroke="#b6ece0" stroke-width="1.2"/>
  </svg>

  <div class="brand brand-hero">ELM<br>COOP</div>
  <div class="abs kicker">Ecommerce Business</div>
  <div class="abs title">Payment</div>

  <!-- Step 2 : payment methods -->
  <section class="panel" style="left:175px;top:338px;height:763px">
    <div class="topbar"><span style="left:514px">English ⌄</span><span style="left:545px">Dollar ⌄</span><span style="left:571px">England ⌄</span></div>
    <div class="masthead">
      <div class="brand">ELM<br>COOP</div>
      <div class="acct" style="left:393px"><i></i>My Account</div>
      <div class="acct" style="left:459px"><i><b></b></i>Wishlist : $350.00</div>
      <div class="acct" style="left:537px"><i><b></b></i>Your Cart : $350.00</div>
    </div>
    <div class="navband"><nav class="navbar"><span class="menu">•••</span><a>Home</a><a class="on">Textbooks</a><a>Computer &amp; Accessories</a><a>Gifts</a><a>stationery</a><a>Laptop</a><a>IT support service</a><span class="find">Search products</span><svg width="8" height="8" viewBox="0 0 8 8"><circle cx="3.3" cy="3.3" r="2.5" fill="none" stroke="#222" stroke-width="1"/><path d="M5.2 5.2 L7.5 7.5" stroke="#222"/></svg></nav></div>
    <div class="crumb">Home &nbsp;›&nbsp; Textbook</div>

    <div class="card" style="top:209px;height:78px">
      <div class="step" style="left:25px"><div class="dot" style="border:none"><svg width="10" height="8"><path d="M1 4 L4 7 L9 1" fill="none" stroke="#c8ccd2" stroke-width="1"/></svg></div><small>FIRST STEP</small><span>Shopping Cart</span></div>
      <div class="step" style="left:160px"><div class="dot on"><svg width="11" height="8"><rect x=".5" y=".5" width="10" height="7" rx="1" fill="none" stroke="#fff"/><path d="M.5 3h10" stroke="#fff"/></svg></div><small>SECOND STEP</small><span>Payment Methods</span></div>
      <div class="step" style="left:307px"><div class="dot"><svg width="11" height="8"><rect x="0" y="1" width="7" height="5" fill="#ccd0d6"/><path d="M7 2h2.5l1.5 2v2H7z" fill="#ccd0d6"/></svg></div><small>THIRD STEP</small><span>Delivery Methods</span></div>
      <div class="step" style="left:452px"><div class="dot"><svg width="10" height="8"><path d="M1 4 L4 7 L9 1" fill="none" stroke="#c8ccd2" stroke-width="1"/></svg></div><small>FOURTH STEP</small><span>Confirmation</span></div>
    </div>

    <div class="card" style="top:304px;height:361px">
      <div class="pay" style="left:194px;background:#1a4fa0">Varda</div>
      <div class="pay" style="left:251px;background:#223a70">Meridian</div>
      <div class="pay" style="left:308px;background:#2b9bd8">Lumbix</div>
      <div class="pay" style="left:365px;background:#222">Orbica</div>
      <div class="abs" style="left:251px;top:45px;width:25px;height:1px;background:var(--blue)"></div>
      <div class="abs rule" style="top:46px"></div>

      <div class="abs" style="left:134px;top:95px;width:315px;height:141px;background:#fff;box-shadow:0 2px 12px rgba(0,0,0,.07)">
        <div class="lbl" style="left:18px;top:20px">Cardholder name</div>
        <div class="lbl" style="left:168px;top:20px">Card number</div>
        <div class="field" style="left:16px;top:34px;width:134px">Name</div>
        <div class="field" style="left:165px;top:34px;width:135px">Name</div>
        <div class="lbl" style="left:18px;top:83px">Expire Date</div>
        <div class="lbl" style="left:218px;top:83px">Card number</div>
        <div class="field sel" style="left:16px;top:98px;width:83px">MM</div>
        <div class="field sel" style="left:116px;top:98px;width:84px">YYYY</div>
        <div class="field" style="left:216px;top:98px;width:84px">Name</div>
      </div>

      <div class="abs rule" style="top:286px"></div>
      <div class="btn ghost" style="left:201px;top:311px;width:83px"><svg width="11" height="8"><path d="M10 4H1M4 1L1 4l3 3" fill="none" stroke="#b4b8bf"/></svg>SHOPPING</div>
      <div class="btn solid" style="left:300px;top:311px;width:79px">DELIVERY<svg width="11" height="8"><path d="M1 4h9M7 1l3 3-3 3" fill="none" stroke="#fff"/></svg></div>
    </div>
  </section>

  <!-- Step 3 : delivery methods -->
  <section class="panel" style="left:175px;top:1132px;height:763px">
    <div class="card" style="top:37px;height:78px">
      <div class="step" style="left:25px"><div class="dot"><svg width="10" height="8"><path d="M1 4 L4 7 L9 1" fill="none" stroke="#c8ccd2" stroke-width="1"/></svg></div><small>FIRST STEP</small><span>Shopping Cart</span></div>
      <div class="step" style="left:160px"><div class="dot"><svg width="11" height="8"><rect x=".5" y=".5" width="10" height="7" rx="1" fill="none" stroke="#ccd0d6"/><path d="M.5 3h10" stroke="#ccd0d6"/></svg></div><small>SECOND STEP</small><span>Payment Methods</span></div>
      <div class="step" style="left:307px"><div class="dot on"><svg width="11" height="8"><rect x="0" y="1" width="7" height="5" fill="#fff"/><path d="M7 2h2.5l1.5 2v2H7z" fill="#fff"/></svg></div><small>THIRD STEP</small><span>Delivery Methods</span></div>
      <div class="step" style="left:452px"><div class="dot"><svg width="10" height="8"><path d="M1 4 L4 7 L9 1" fill="none" stroke="#c8ccd2" stroke-width="1"/></svg></div><small>FOURTH STEP</small><span>Confirmation</span></div>
    </div>

    <div class="card" style="top:132px;height:506px">
      <div class="cap" style="left:228px;top:19px;font-size:5.5px">Free Delivery</div>
      <div class="cap" style="left:319px;top:19px;font-size:5.5px;color:var(--blue);font-weight:500">Express Delivery</div>
      <div class="abs" style="left:308px;top:45px;width:63px;height:1px;background:var(--blue)"></div>
      <div class="abs rule" style="top:46px"></div>

      <div class="lbl" style="left:152px;top:83px">First name</div>
      <div class="lbl" style="left:302px;top:83px">Last name</div>
      <div class="field" style="left:150px;top:100px;width:134px">Tom</div>
      <div class="field" style="left:299px;top:100px;width:135px">Reyes</div>

      <div class="lbl" style="left:152px;top:146px">Country</div>
      <div class="lbl" style="left:252px;top:146px">City</div>
      <div class="lbl" style="left:352px;top:146px">State</div>
      <div class="field sel" style="left:150px;top:163px;width:83px">USA</div>
      <div class="field" style="left:250px;top:163px;width:84px">Westfield</div>
      <div class="field" style="left:350px;top:163px;width:84px">Oregon</div>

      <div class="lbl" style="left:152px;top:210px">Zip Code</div>
      <div class="lbl" style="left:252px;top:210px">Address</div>
      <div class="field" style="left:150px;top:226px;width:83px">97001</div>
      <div class="field" style="left:250px;top:226px;width:156px">27 Cedar Row, Westfield, OR 97001</div>

      <div class="lbl" style="left:152px;top:273px">Phone</div>
      <div class="lbl" style="left:302px;top:273px">Email</div>
      <div class="field" style="left:150px;top:290px;width:134px">(555) 014-2290</div>
      <div class="field" style="left:299px;top:290px;width:135px">tom.reyes@mailnest.com</div>

      <div class="opt on" style="left:150px;top:331px"><em>Skyway delivery</em><small>10-12 Days</small><strong>$ 80.67</strong></div>
      <div class="opt" style="left:299px;top:331px"><em>Northpost delivery</em><small>10-15 Days</small><strong>$ 80.67</strong></div>

      <div class="abs rule" style="top:426px"></div>
      <div class="btn ghost" style="left:201px;top:453px;width:83px"><svg width="11" height="8"><path d="M10 4H1M4 1L1 4l3 3" fill="none" stroke="#b4b8bf"/></svg>SHOPPING</div>
      <div class="btn solid" style="left:300px;top:453px;width:79px">DELIVERY<svg width="11" height="8"><path d="M1 4h9M7 1l3 3-3 3" fill="none" stroke="#fff"/></svg></div>
    </div>
  </section>

  <!-- Step 4 : confirmation -->
  <section class="panel" style="left:1002px;top:265px;height:1592px">
    <div class="topbar"><span style="left:514px">English ⌄</span><span style="left:545px">Dollar ⌄</span><span style="left:571px">England ⌄</span></div>
    <div class="masthead">
      <div class="brand">ELM<br>COOP</div>
      <div class="acct" style="left:393px"><i></i>My Account</div>
      <div class="acct" style="left:459px"><i><b></b></i>Wishlist : $350.00</div>
      <div class="acct" style="left:537px"><i><b></b></i>Your Cart : $350.00</div>
    </div>
    <div class="navband"><nav class="navbar"><span class="menu">•••</span><a>Home</a><a class="on">Textbooks</a><a>Computer &amp; Accessories</a><a>Gifts</a><a>stationery</a><a>Laptop</a><a>IT support service</a><span class="find">Search products</span><svg width="8" height="8" viewBox="0 0 8 8"><circle cx="3.3" cy="3.3" r="2.5" fill="none" stroke="#222" stroke-width="1"/><path d="M5.2 5.2 L7.5 7.5" stroke="#222"/></svg></nav></div>
    <div class="crumb">Home &nbsp;›&nbsp; Textbook</div>

    <div class="card" style="top:208px;height:78px">
      <div class="step" style="left:25px"><div class="dot"><svg width="10" height="8"><path d="M1 4 L4 7 L9 1" fill="none" stroke="#c8ccd2" stroke-width="1"/></svg></div><small>FIRST STEP</small><span>Shopping Cart</span></div>
      <div class="step" style="left:160px"><div class="dot"><svg width="11" height="8"><rect x=".5" y=".5" width="10" height="7" rx="1" fill="none" stroke="#ccd0d6"/><path d="M.5 3h10" stroke="#ccd0d6"/></svg></div><small>SECOND STEP</small><span>Payment Methods</span></div>
      <div class="step" style="left:307px"><div class="dot"><svg width="11" height="8"><rect x="0" y="1" width="7" height="5" fill="#ccd0d6"/><path d="M7 2h2.5l1.5 2v2H7z" fill="#ccd0d6"/></svg></div><small>THIRD STEP</small><span>Delivery Methods</span></div>
      <div class="step" style="left:452px"><div class="dot on"><svg width="10" height="8"><path d="M1 4 L4 7 L9 1" fill="none" stroke="#fff" stroke-width="1.2"/></svg></div><small>FOURTH STEP</small><span>Confirmation</span></div>
    </div>

    <div class="card" style="top:303px;height:648px">
      <svg class="abs" style="left:70px;top:50px" width="11" height="10"><path d="M0 1h2l2 6h6l1-4H3" fill="none" stroke="#c3c7ce"/><circle cx="5" cy="9" r="1" fill="#c3c7ce"/><circle cx="9" cy="9" r="1" fill="#c3c7ce"/></svg>
      <div class="sec" style="left:115px;top:52px">SHOPPING CART</div>
      <div class="abs" style="left:99px;top:78px;width:385px;height:1px;background:var(--line)"></div>
      <div class="row" style="left:115px;top:99px">Importance Of The Custom Company Logo Design</div>
      <div class="row" style="left:342px;top:99px">$ 83.56</div>
      <div class="row m" style="left:392px;top:99px">2 items</div>
      <div class="row" style="left:438px;top:99px">$ 167.23</div>
      <div class="abs" style="left:99px;top:127px;width:385px;height:1px;background:var(--line)"></div>
      <div class="row" style="left:115px;top:146px">Study 800 Numbers Still Popular With Advertisers</div>
      <div class="row" style="left:342px;top:146px">$ 32.34</div>
      <div class="row m" style="left:392px;top:146px">1 items</div>
      <div class="row" style="left:442px;top:146px">$ 32.34</div>
      <div class="abs" style="left:99px;top:174px;width:385px;height:1px;background:var(--line)"></div>

      <svg class="abs" style="left:70px;top:209px" width="11" height="8"><rect x=".5" y=".5" width="10" height="7" rx="1" fill="none" stroke="#c3c7ce"/><path d="M.5 3h10" stroke="#c3c7ce"/></svg>
      <div class="sec" style="left:115px;top:210px">PAYMENT INFO</div>
      <div class="abs" style="left:99px;top:237px;width:385px;height:1px;background:var(--line)"></div>
      <div class="abs" style="left:115px;top:253px;width:26px;height:16px;background:#223a70;border-radius:1px"></div>
      <div class="row" style="left:152px;top:257px">Meridian Card Credit</div>
      <div class="row" style="left:370px;top:257px;letter-spacing:1.2px">XXXX-XXXX-XXXX-6532</div>
      <div class="abs" style="left:99px;top:284px;width:385px;height:1px;background:var(--line)"></div>

      <svg class="abs" style="left:70px;top:319px" width="11" height="8"><rect x="0" y="1" width="7" height="5" fill="#c3c7ce"/><path d="M7 2h2.5l1.5 2v2H7z" fill="#c3c7ce"/></svg>
      <div class="sec" style="left:115px;top:320px">SHIPPING INFO</div>
      <div class="abs" style="left:99px;top:347px;width:385px;height:1px;background:var(--line)"></div>
      <div class="cap" style="left:115px;top:363px">Name:</div><div class="cap" style="left:183px;top:363px">Phone:</div><div class="cap" style="left:268px;top:363px">Country:</div><div class="cap" style="left:350px;top:363px">Email:</div>
      <div class="row" style="left:115px;top:379px">Tom Reyes</div><div class="row" style="left:183px;top:379px">555-014-2290</div><div class="row" style="left:268px;top:379px">USA</div><div class="row" style="left:350px;top:379px">tom.reyes@mailnest.com</div>
      <div class="cap" style="left:115px;top:400px">City:</div><div class="cap" style="left:183px;top:400px">State:</div><div class="cap" style="left:268px;top:400px">Zip Code:</div><div class="cap" style="left:350px;top:400px">Address:</div>
      <div class="row" style="left:115px;top:416px">Westfield</div><div class="row" style="left:183px;top:416px">Oregon</div><div class="row" style="left:268px;top:416px">97001</div><div class="row" style="left:350px;top:416px">18 Harbor Lane Suite 210</div>
      <div class="abs" style="left:99px;top:442px;width:385px;height:1px;background:var(--line)"></div>
      <div class="row" style="left:115px;top:463px">Premium Shipping Skyway delivery</div>
      <div class="row m" style="left:350px;top:463px">10-12 Days</div>
      <div class="row" style="left:443px;top:463px">$ 80.67</div>
      <div class="abs" style="left:99px;top:489px;width:385px;height:1px;background:var(--line)"></div>
      <div class="row" style="left:378px;top:519px;font-size:6.5px;color:#666">Total price:</div>
      <div class="row" style="left:426px;top:513px;font-size:14px;font-weight:500">$ 941.05</div>

      <div class="abs rule" style="top:569px"></div>
      <div class="btn ghost" style="left:185px;top:597px;width:83px"><svg width="8" height="6"><path d="M7 3H1M3 1L1 3l2 2" fill="none" stroke="#b4b8bf"/></svg>DELIVERY</div>
      <div class="btn solid" style="left:284px;top:597px;width:133px">PROCEED TO CHECKOUT<svg width="8" height="6"><path d="M1 3h6M5 1l2 2-2 2" fill="none" stroke="#fff"/></svg></div>
    </div>

    <!-- contact -->
    <div class="abs" style="left:0;top:1000px;width:100%;height:330px;background:#fff"></div>
    <div class="field" style="left:146px;top:1110px;width:226px;height:23px;line-height:21px;color:#aaa">Email Address*</div>
    <div class="field" style="left:146px;top:1141px;width:226px;height:23px;line-height:21px;color:#aaa">Subject*</div>
    <div class="field" style="left:146px;top:1173px;width:226px;height:73px;line-height:21px;color:#aaa">Your Message*</div>
    <div class="btn solid" style="left:146px;top:1256px;width:77px;height:19px;font-size:6px;letter-spacing:0;font-weight:500">Learn more</div>
    <div class="abs" style="left:411px;top:1105px;font-size:16px;line-height:21px;color:var(--ink);width:180px">Don’t Hesitate to contact with us for any kind of information</div>
    <div class="abs" style="left:411px;top:1177px;font-size:6px;color:var(--muted)">Call us for imidiate support to this number</div>
    <div class="abs" style="left:411px;top:1202px;font-size:10px;color:var(--ink)">000 123 456 7890</div>
    <svg class="abs" style="left:410px;top:1231px" width="60" height="16"><circle cx="8" cy="8" r="6.5" fill="none" stroke="var(--blue)"/><circle cx="28" cy="8" r="6.5" fill="none" stroke="#ddd"/><circle cx="48" cy="8" r="6.5" fill="none" stroke="#ddd"/></svg>

    <!-- newsletter -->
    <div class="abs" style="left:0;top:1330px;width:100%;height:152px;background:#f3f4f7"></div>
    <div class="abs" style="left:184px;top:1360px;width:92px;height:67px;background:#fff"><div class="brand" style="left:25px;top:19px;font-size:15px;letter-spacing:0">ELM<br>COOP</div></div>
    <div class="abs" style="left:336px;top:1368px;font-size:10px;line-height:11px;color:var(--ink);width:190px">The magnetic behavior of a material depends on its structure</div>
    <div class="field" style="left:336px;top:1401px;width:160px;height:19px;line-height:17px;font-size:5.5px;color:#aaa">Enter your E-mail ID</div>
    <div class="btn solid" style="left:496px;top:1401px;width:58px;height:19px;font-size:5px;letter-spacing:.3px">SUBSCRIBE</div>

    <!-- footer -->
    <div class="abs" style="left:0;top:1482px;width:100%;height:110px;background:var(--foot)">
      <div class="foot-col" style="left:146px"><b>Address</b>PO Box 1024 Harbor Street<br>Westfield 9700 – Map<br>+00 0 1234 5678<br>hello@elmcoop.edu</div>
      <div class="foot-col" style="left:248px"><b>About us</b>Our Story<br>Contact us<br>Policy<br>Career</div>
      <div class="foot-col" style="left:307px"><b>Shop by</b>New Arrival<br>Best Seller<br>Features Product<br>Sale Off</div>
      <div class="foot-col" style="left:376px"><b>Support</b>The Blog<br>FAQs<br>Order Tracking<br>Shipping and Returns</div>
      <div class="foot-col" style="left:454px"><b>Secure Payment</b></div>
      <svg class="abs" style="left:454px;top:36px" width="125" height="8"><rect x="0" y="0" width="14" height="8" rx="1" fill="#5b7fd1"/><rect x="27" y="0" width="14" height="8" rx="1" fill="#e9843b"/><rect x="54" y="0" width="14" height="8" rx="1" fill="#3a68d8"/><rect x="81" y="0" width="14" height="8" rx="1" fill="#4a7be0"/><rect x="108" y="0" width="14" height="8" rx="1" fill="#4d8fe8"/></svg>
      <svg class="abs" style="left:146px;top:80px" width="62" height="10"><circle cx="5" cy="5" r="4.5" fill="#3b64c4"/><circle cx="16" cy="5" r="4.5" fill="#3aa0e8"/><circle cx="27" cy="5" r="4.5" fill="#e04040"/><circle cx="38" cy="5" r="4.5" fill="#555"/><circle cx="49" cy="5" r="4.5" fill="#e25a8c"/></svg>
      <div class="abs" style="left:454px;top:82px;font-size:4px;color:#c7cad2">Copyright by elm</div>
    </div>
  </section>

  <div class="badge" style="left:865px;top:279px">2</div>
  <div class="badge" style="left:865px;top:1148px">3</div>
  <div class="badge" style="left:1696px;top:201px">4</div>
</div>
</body>
</html>
```